Korvex Systems*

Stationary design including business cards, letter heads, envelops and email signatures using our new logo

Target Market(s)

Innovative Technologies

Industry/Entity Type

Defense Contracting

Font styles to use
Sans Serif

```html
<!DOCTYPE html>
<html lang="en">
<head>
<meta charset="utf-8">
<title>Korvex Systems – Business Card</title>
<link rel="stylesheet" href="https://fonts.googleapis.com/css2?family=Oswald:wght@400;700&family=Roboto:wght@400&display=swap">
<style>
  :root {
    --backdrop: #d9d9da;
    --card-white: #ffffff;
    --card-black: #0b0b0b;
    --ink: #111111;
    --ink-soft: #3a3a3a;
    --paper-ink: #f4f4f4;
  }
  * { box-sizing: border-box; margin: 0; padding: 0; }
  html, body { width: 1200px; height: 813px; overflow: hidden; }
  body {
    background: var(--backdrop);
    font-family: "Roboto", sans-serif;
    display: flex; align-items: center; justify-content: center; gap: 48px;
  }
  .card {
    width: 530px; height: 303px; border-radius: 26px;
    position: relative; box-shadow: 0 10px 24px rgba(0,0,0,.18);
  }
  .card--front { background: var(--card-white); color: var(--ink); }
  .card--back { background: var(--card-black); color: var(--paper-ink);
    display: flex; align-items: center; justify-content: center; }

  .brand { display: flex; align-items: center; gap: 10px;
    font-family: "Oswald", sans-serif; font-weight: 400; text-transform: uppercase; letter-spacing: .5px; }
  .brand__mark { width: 14px; height: 14px; border: 2px solid currentColor; }
  .card--front .brand { position: absolute; top: 44px; left: 0; right: 0; justify-content: center; font-size: 30px; }
  .card--back .brand { font-size: 40px; }
  .card--back .brand__mark { width: 18px; height: 18px; }

  .details { position: absolute; top: 128px; left: 0; right: 0;
    display: flex; justify-content: center; align-items: center; }
  .person { text-align: right; padding-right: 22px; }
  .person__name { font-family: "Oswald", sans-serif; font-weight: 700; font-size: 24px; letter-spacing: 1.5px; text-transform: uppercase; line-height: 1.1; }
  .person__role { font-size: 15px; color: var(--ink-soft); margin-top: 4px; }
  .divider { width: 1px; height: 76px; background: var(--ink); }
  .contacts { list-style: none; padding-left: 22px; font-size: 14.5px; color: var(--ink-soft); }
  .contacts li { display: flex; align-items: center; gap: 8px; line-height: 1.55; }
  .contacts svg { width: 13px; height: 13px; fill: var(--ink); flex: none; }
  .address { position: absolute; bottom: 40px; left: 0; right: 0; text-align: center; font-size: 15px; color: var(--ink-soft); }
</style>
</head>
<body>
  <section class="card card--front">
    <div class="brand"><span class="brand__mark"></span><span>Korvex Systems</span></div>
    <div class="details">
      <div class="person">
        <p class="person__name">Daniel Hartley</p>
        <p class="person__role">Executive Director</p>
      </div>
      <div class="divider"></div>
      <ul class="contacts">
        <li><svg viewBox="0 0 24 24" aria-hidden="true"><path d="M6.6 10.8a15 15 0 0 0 6.6 6.6l2.2-2.2a1 1 0 0 1 1-.25 11.4 11.4 0 0 0 3.6.57 1 1 0 0 1 1 1V20a1 1 0 0 1-1 1A17 17 0 0 1 3 4a1 1 0 0 1 1-1h3.5a1 1 0 0 1 1 1c0 1.25.2 2.45.57 3.57a1 1 0 0 1-.25 1z"/></svg>+1234-5550-0188</li>
        <li><svg viewBox="0 0 24 24" aria-hidden="true"><path d="M2 5h20v14H2z M2 5l10 8 10-8" /></svg>info@korvexsystems.com</li>
        <li><svg viewBox="0 0 24 24" aria-hidden="true"><circle cx="12" cy="12" r="10"/></svg>www.korvexsystems.com</li>
      </ul>
    </div>
    <p class="address">P.O. Box: 48210, Linden Row, London, United Kingdom</p>
  </section>

  <section class="card card--back">
    <div class="brand"><span class="brand__mark"></span><span>Korvex Systems</span></div>
  </section>
</body>
</html>
```